New Business Cards for Organic Meat Farm

We need a business card designed for Quillmoor Farm, a meat farm in western MA. Our logo uses a hand-drawn woodcut (attached). Our color palette has been simply black and white (shown in notepad and picture of our food truck). While we are based out of western MA, we have ambitions to grow nationally, so our hope is for a classy and memorable card which will be printed on a premium quality stock from a printer like printkestrel.com.
Target Market(s)
consumers of quality meats, restauranteurs, partnering farms
Industry/Entity Type
Farming and prepared meat products
Contact Information for Business Card
Corbin Alderfell, President/Owner, corbin@quillmoorfarm.com, mobile: 413-555-0172, phone: 413-555-0148, quillmoorfarm.com, facebook: @quillmoorfarm, instagram: @quillmoorfarmma
Colors
Designer to choose colors to be used in the design.
Look and feel

```html
<!DOCTYPE html>
<html lang="en">
<head>
<meta charset="utf-8">
<title>Quillmoor Farm – Business Card</title>
<link href="https://fonts.googleapis.com/css2?family=Jost:wght@400;500;600;700&display=swap" rel="stylesheet">
<style>
  :root {
    --backdrop: #6e6e70;
    --card: #232324;
    --gloss: #141415;
    --gloss-soft: #2e2e30;
    --ink: #ffffff;
    --ink-soft: #e6e6e6;
    --woodcut-light: #dcdcdc;
    --woodcut-mid: #9a9a9a;
  }
  * { margin: 0; padding: 0; box-sizing: border-box; }
  html, body {
    width: 900px; height: 1200px; overflow: hidden;
    background: var(--backdrop);
    font-family: 'Jost', sans-serif;
  }
  .card {
    position: absolute;
    left: 135px;
    width: 630px; height: 358px;
    background: var(--card);
    border-radius: 12px;
  }
  .card--front { top: 215px; }
  .card--back { top: 628px; }

  .woodcut {
    position: absolute;
    border-radius: 50% 50% 6px 6px / 70% 70% 6px 6px;
  }
  .card--front .woodcut {
    left: 165px; top: 33px; width: 293px; height: 127px;
    background: linear-gradient(160deg, var(--gloss-soft), var(--gloss) 70%);
  }
  .card--back .woodcut {
    left: 366px; top: 92px; width: 211px; height: 90px;
    background: linear-gradient(160deg, var(--woodcut-light), var(--woodcut-mid));
  }

  .brand__name, .brand__est {
    position: absolute; text-align: center; white-space: nowrap; line-height: 1;
  }
  .brand__name { font-weight: 600; letter-spacing: 0.1em; }
  .brand__est { font-weight: 500; letter-spacing: 0.14em; }

  .card--front .brand__name { left: 0; right: 0; top: 192px; font-size: 27px; color: var(--gloss); }
  .card--front .brand__est { left: 0; right: 0; top: 303px; font-size: 11px; color: #1b1b1c; }

  .card--back .brand__name { left: 352px; width: 240px; top: 208px; font-size: 19px; color: var(--ink-soft); }
  .card--back .brand__est { left: 352px; width: 240px; top: 275px; font-size: 9px; color: var(--ink-soft); }

  .contact { position: absolute; left: 56px; top: 78px; color: var(--ink); }
  .contact__name { font-size: 27px; font-weight: 700; letter-spacing: 0.02em; line-height: 1; }
  .contact__title {
    font-size: 16.5px; font-weight: 400; line-height: 1.2; margin-top: 4px;
    padding-bottom: 3px; border-bottom: 1px solid var(--ink); width: 136px;
  }
  .contact__list { list-style: none; margin-top: 3px; }
  .contact__item {
    display: flex; align-items: center; gap: 6px;
    font-size: 17px; font-weight: 400; letter-spacing: 0.03em;
    height: 25.3px; white-space: nowrap;
  }
  .contact__icon { width: 12px; height: 12px; flex: none; fill: var(--ink); }
</style>
</head>
<body>

<section class="card card--front" aria-label="Card front">
  <div class="woodcut" role="img" aria-label="Woodcut illustration of the farmhouse, gloss black on black"></div>
  <div class="brand__name">QUILLMOOR FARM</div>
  <div class="brand__est">EST. 1904</div>
</section>

<section class="card card--back" aria-label="Card back">
  <div class="contact">
    <div class="contact__name">CORBIN ALDERFELL</div>
    <div class="contact__title">President/Owner</div>
    <ul class="contact__list">
      <li class="contact__item">
        <svg class="contact__icon" viewBox="0 0 12 12"><path d="M2.5 0.8l2 2-1 1.5c.7 1.5 1.8 2.6 3.2 3.2l1.5-1 2 2-1.2 2C5.5 10.3 1.7 6.5 0.5 2z"/></svg>
        413-555-0148
      </li>
      <li class="contact__item">
        <svg class="contact__icon" viewBox="0 0 12 12"><rect x="2.5" y="0" width="7" height="12" rx="1.2"/><rect x="3.6" y="1.4" width="4.8" height="8" fill="#232324"/></svg>
        413-555-0172
      </li>
      <li class="contact__item">
        <svg class="contact__icon" viewBox="0 0 12 12"><rect x="0" y="2" width="12" height="8.5" rx="1"/><path d="M0.5 2.6L6 6.8l5.5-4.2" stroke="#232324" stroke-width="1.2" fill="none"/></svg>
        corbin@quillmoorfarm.com
      </li>
      <li class="contact__item">
        <svg class="contact__icon" viewBox="0 0 12 12"><circle cx="6" cy="6" r="5.5"/><path d="M0.5 6h11M6 0.5c-3 3-3 8 0 11M6 0.5c3 3 3 8 0 11" stroke="#232324" stroke-width="1" fill="none"/></svg>
        quillmoorfarm.com
      </li>
      <li class="contact__item">
        <svg class="contact__icon" viewBox="0 0 12 12"><circle cx="6" cy="6" r="5.5"/></svg>
        @quillmoorfarm
      </li>
      <li class="contact__item">
        <svg class="contact__icon" viewBox="0 0 12 12"><circle cx="6" cy="6" r="5.5"/></svg>
        @quillmoorfarmma
      </li>
    </ul>
  </div>

  <div class="woodcut" role="img" aria-label="Woodcut illustration of the farmhouse in white and grey"></div>
  <div class="brand__name">QUILLMOOR FARM</div>
  <div class="brand__est">EST. 1904</div>
</section>

</body>
</html>
```